Solo Law Practice Website Design

I am starting a solo law practice that will specialize in criminal defense and family law.

I have a rudimentary understanding of Wordpress as used through the tidalnest web services. The winning design would be compatible with this system so that I can modify content on my own.

I have supplied the written content and the components that I am looking for at the domain name: morganvaleslaw.com.

I would like to take that content and work it into a website that looks more professional and inviting. The two most important goals of the website are ease of navigation and rich content for search engine spiders (for example, integrating articles into pages rather than linking to a word document).

The winning design should be turnkey for me to upload immediately.
Updates

Reason: I will be traveling.

Target Market(s)

Individuals looking for legal services.

Industry/Entity Type

Defense

Requirements
Must have
• My picture should appear at least once in the site.

The design should allow a space for me to post blog or legal updates. Additionally, there should be functionality for me to add additional articles to the site.
Nice to have
• Appropriate pictures for a legal website to break-up text on pages.

Simple flash features that won't significantly slow loading times.

Widgets that drive traffic to a contact page or function.

```html
<!DOCTYPE html>
<html lang="en">
<head>
<meta charset="utf-8">
<title>Law Offices of Morgan Vales PLLC</title>
<link href="https://fonts.googleapis.com/css2?family=Lato:wght@300;400;700;900&display=swap" rel="stylesheet">
<style>
:root{
  --ink:#111;
  --text:#333;
  --muted:#7a7a7a;
  --label:#8a8a8a;
  --red:#b0180f;
  --red-bright:#c8271b;
  --band:#474543;
  --footer-base:#232323;
  --nav-active:#dcdcdc;
  --rule:#9a9a9a;
  --field:#d8d8d8;
  --white:#fff;
}
*{margin:0;padding:0;box-sizing:border-box}
html,body{width:686px;height:1200px;overflow:hidden;background:var(--white)}
body{font-family:'Lato',sans-serif;color:var(--text)}
.page{position:relative;width:800px;height:1400px;transform:scale(.8575);transform-origin:0 0}
.abs{position:absolute}

.palette{left:7px;top:200px}
.palette span{display:block;width:13px;height:13px;margin-bottom:7px}

.brand{left:80px;top:30px}
.brand-kicker{font-size:10px;font-weight:400;letter-spacing:.3px;color:var(--ink)}
.brand-name{font-size:24px;font-weight:900;color:var(--ink);letter-spacing:.5px;line-height:28px;margin-top:2px}
.brand-name span{color:#bdbdbd;font-weight:700}
.header-contact{left:560px;top:36px;font-size:10px;line-height:18px;color:var(--ink)}
.header-contact b{font-weight:900;margin-right:4px}

.nav{left:80px;top:94px;width:640px;height:39px;background:var(--white);display:flex;font-size:10px;color:var(--text)}
.nav a{display:block;padding:0 8px;line-height:39px;color:inherit;text-decoration:none}
.nav a:first-child{padding-left:11px}
.nav a.active{background:var(--nav-active)}

.hero{left:80px;top:133px;width:640px;height:267px;overflow:hidden}
.hero-photo{position:absolute;inset:0;background:radial-gradient(ellipse at 35% 45%,#dcdcdc 0%,#9c9c9c 45%,#444 100%)}
.hero-red{position:absolute;inset:0}
.hero-text{position:absolute;left:380px;top:153px;color:var(--white);line-height:25px}
.hero-text .lead{font-size:19px;font-weight:300;letter-spacing:.5px}
.hero-text .big{font-size:26px;font-weight:900;letter-spacing:.3px}

.tagline{left:80px;top:400px;width:640px;height:87px;background:var(--band);color:var(--white);text-align:center;font-size:20px;font-weight:300;line-height:24px;padding-top:18px}

.feature{top:510px;width:190px}
.feature h2{font-size:16px;font-weight:400;color:var(--text);margin-bottom:8px}
.feature .shot{width:187px;height:87px;display:block}
.feature p{font-size:9.5px;line-height:14.5px;color:var(--muted);margin-top:15px}

.section-title{font-size:17px;font-weight:400;color:var(--text);padding-bottom:7px;border-bottom:2px solid var(--rule)}
.areas{left:93px;top:750px;width:406px}
.area h3{font-size:13px;font-weight:400;color:var(--red-bright);margin:22px 0 6px 1px}
.area p{font-size:9.5px;line-height:14.5px;color:var(--muted)}

.contact{left:520px;top:750px;width:187px}
.contact label{display:block;font-size:9px;color:var(--label);margin-top:10px}
.contact .field{width:133px;height:17px;border:1px solid var(--field);margin-top:4px}
.contact .choice{display:flex;gap:30px;font-size:9px;color:var(--text);margin-top:6px;align-items:center}
.contact .choice span{display:flex;align-items:center;gap:8px}
.radio{width:10px;height:10px;border-radius:50%;border:1px solid #bbb;display:inline-block;position:relative}
.radio.on::after{content:"";position:absolute;left:2px;top:2px;width:4px;height:4px;border-radius:50%;background:#555}
.contact .message{width:187px;height:100px;border:1px solid var(--field);margin-top:6px}
.btn{background:var(--red-bright);color:var(--white);font-size:8px;font-weight:700;border:1px solid #8e130c;text-align:center}
.submit{position:absolute;left:139px;top:309px;width:48px;height:21px;line-height:19px}

.footer{left:80px;top:1100px;width:640px;height:200px;background:var(--band);color:var(--white)}
.footer-col{position:absolute;top:18px;width:180px}
.footer-col h2{font-size:15px;font-weight:400;margin-bottom:11px}
.footer-col p{font-size:9px;line-height:14.5px}
.subscribe{display:flex;margin-top:13px}
.subscribe .email{width:133px;height:20px;background:#8b8989;border:1px solid #9f9d9b;font-size:8px;line-height:18px;padding-left:7px}
.subscribe .btn{width:46px;height:20px;line-height:18px;margin-left:7px;border:none}
.bottom{left:80px;top:1300px;width:640px;height:66px;background:var(--footer-base);color:var(--white);text-align:center;font-size:9px;line-height:14px;padding-top:18px}
</style>
</head>
<body>
<div class="page">

  <div class="abs palette" aria-hidden="true">
    <span style="background:#111"></span>
    <span style="background:#a51a14"></span>
    <span style="background:#aaa"></span>
    <span style="background:#ddd"></span>
    <span style="background:#444"></span>
  </div>

  <header class="abs brand">
    <div class="brand-kicker">LAW OFFICES OF</div>
    <div class="brand-name">MORGAN VALES <span>PLLC</span></div>
  </header>
  <div class="abs header-contact">
    <div><b>PHONE:</b> (612) 555-0147</div>
    <div><b>EMAIL:</b> Morgan@MorganValesLaw.com</div>
  </div>

  <nav class="abs nav">
    <a>Home</a><a>Contact Me</a><a>Criminal Law</a><a class="active">Family Law</a><a>Will Drafting</a><a>Attorney Profile</a><a>Fees</a><a>Legal Updates</a><a>Online Resources</a><a>Articles</a>
  </nav>

  <section class="abs hero">
    <div class="hero-photo" role="img" aria-label="Portrait photograph of the attorney in shirt and tie, black and white"></div>
    <svg class="hero-red" width="640" height="267" viewBox="0 0 640 267" aria-hidden="true">
      <defs>
        <linearGradient id="redGlow" x1="1" y1="0" x2="0" y2="1">
          <stop offset="0" stop-color="#cc2a1c"/>
          <stop offset="1" stop-color="#9c120c"/>
        </linearGradient>
      </defs>
      <polygon points="393,0 640,0 640,267 353,267" fill="url(#redGlow)"/>
    </svg>
    <div class="hero-text">
      <div class="lead">SPECIALIZING IN</div>
      <div class="big">CRIMINAL DEFENSE</div>
      <div class="big">AND FAMILY LAW</div>
    </div>
  </section>

  <div class="abs tagline">Practice&nbsp; focused on accomplishing your goals<br>through results-oriented work at a discount price</div>

  <section class="abs feature" style="left:91px">
    <h2>Personal Attention.</h2>
    <div class="shot" role="img" aria-label="Photo of two people shaking hands" style="background:linear-gradient(90deg,#3a4150,#e9ecef 45%,#eef0f2 55%,#2e3440)"></div>
    <p>I control the size of my practice so that I am able to devote 100% of my effort to each case. I have no “associates” so I handle every case personally.</p>
  </section>
  <section class="abs feature" style="left:307px">
    <h2>General Practice</h2>
    <div class="shot" role="img" aria-label="Photo of a lawyer in front of bookshelves" style="background:linear-gradient(90deg,#1d3550,#8c7c6c 45%,#2a3f5a 75%,#10243a)"></div>
    <p>I am available to provide your defense if you are accused of a felony or misdemeanor.&nbsp; Additionally, I can work with you on family matters such as divorce, child custody, wills, and nuptial agreements.</p>
  </section>
  <section class="abs feature" style="left:520px">
    <h2>Free first consultation</h2>
    <div class="shot" role="img" aria-label="Photo of a couple meeting with a lawyer" style="background:linear-gradient(90deg,#e8e8e8,#9a9a9a 50%,#c84a44 80%,#efefef)"></div>
    <p>I will take time to listen to your individual situation.&nbsp; I will explain the legal issues, and the risks involved in each course of action we may pursue so that you can make informed decisions about how to proceed.</p>
  </section>

  <section class="abs areas">
    <h2 class="section-title">Areas of specialization</h2>
    <div class="area">
      <h3>CRIMINAL LAW</h3>
      <p>Convictions carry serious consequences and can often have a negative financial impact as well as putting your freedom in jeopardy.&nbsp; I know how to work on your behalf because I used to work at the Lakeshore County Attorney’s Office and appeared on the prosecution’s behalf for more than 600 cases.&nbsp; I will prepare your defense, negotiate plea bargains if desired, or take the case to trial.</p>
    </div>
    <div class="area">
      <h3 style="margin-top:25px">EXPERIENCE MATTERS</h3>
      <p>Every case is different.&nbsp; You can take comfort knowing that I have appeared in court on a wide variety of cases including assault, drug possession and distribution, DWI, disorderly conduct, theft, burglary, domestic assault, check forgery, violations or orders for protection, firearms violations and DWI test refusals.&nbsp; I am also prepared to handle your probation violation or expungement.</p>
    </div>
    <div class="area">
      <h3 style="margin-top:27px">FAMILY LAW</h3>
      <p>I am prepared to handle your family law concerns.&nbsp; I can guide you through the process of child custody matters, divorce, wills and nuptial agreements to ensure that you receive a fair and equitable result on these sensitive matters.</p>
    </div>
  </section>

  <section class="abs contact">
    <h2 class="section-title">Contact Me</h2>
    <label>Your Name</label><div class="field"></div>
    <label>Your Phone</label><div class="field"></div>
    <label>Your Email</label><div class="field"></div>
    <label style="margin-top:13px">Preferred mode of contact</label>
    <div class="choice"><span><i class="radio on"></i>Phone</span><span><i class="radio"></i>Email</span></div>
    <label>Briefly describe your legal issue</label>
    <div class="message"></div>
    <div class="btn submit">SUBMIT</div>
  </section>

  <footer class="abs footer">
    <div class="footer-col" style="left:14px">
      <h2>About Me</h2>
      <p>My practice is focused on accomplishing your goals through results-oriented work at a discount price.&nbsp; For your convenience, I handle legal matters throughout the Twin Cities, including Hennepin, Ramsey, Anoka, and Washington counties.&nbsp; I understand that legal issues can appear complicated, and that is why I take a hands-on approach to guiding you through your legal needs.</p>
    </div>
    <div class="footer-col" style="left:227px">
      <h2>Subscribe</h2>
      <p>Enter your email address to receive notifications of legal updates by e-mail.</p>
      <div class="subscribe"><div class="email">Enter email here</div><div class="btn">Submit</div></div>
    </div>
    <div class="footer-col" style="left:440px">
      <h2>Contact Me</h2>
      <p>Looking for legal representation? I offer Free consultation. You can contact me&nbsp; via any of the following option.</p>
      <p style="margin-top:14px">Phone:&nbsp; 612 555 0147<br>Email : morgan@morganvaleslaw.com</p>
    </div>
  </footer>
  <div class="abs bottom">morganvaleslaw.com © 2012 Law Offices of Morgan Vales PLLC<br>Delivering legal services in the greater Twin Cities area.</div>

</div>
</body>
</html>
```